hfdhddfgfhfghfghgfhfhfhgfhfhfh

Industry/Entity Type

Painting

Logo Text

TOLVEN Painting

Logo styles of interest
Wordmark Logo
Requirements
Should not have
• Paintbrushes or rollers etc....

```html
<!DOCTYPE html>
<html lang="en">
<head>
<meta charset="utf-8">
<title>TOLVEN Painting – Business Card</title>
<link href="https://fonts.googleapis.com/css2?family=Poiret+One&display=swap" rel="stylesheet">
<style>
  :root {
    --brand-blue: #003091;
    --paper: #ffffff;
    --ink: #000000;
    --card-font: "Poiret One", sans-serif;
  }
  * { margin: 0; padding: 0; box-sizing: border-box; }
  html, body {
    width: 1200px; height: 900px; overflow: hidden;
    background: var(--brand-blue);
  }
  .card {
    position: relative;
    width: 1200px; height: 900px;
    background: var(--brand-blue);
    font-family: var(--card-font);
  }
  .brand-panel {
    position: absolute;
    left: 10px; top: 10px;
    width: 1180px; height: 424px;
    background: var(--paper);
    display: flex;
    align-items: center;
    justify-content: center;
    padding-bottom: 24px;
  }
  .company-name {
    font-family: var(--card-font);
    font-weight: 400;
    font-size: 104px;
    line-height: 1;
    color: var(--ink);
    white-space: nowrap;
  }
  .contact-panel {
    position: absolute;
    left: 8px; top: 452px;
    width: 1184px; height: 440px;
    border: 2px solid var(--paper);
    color: var(--paper);
    text-align: center;
  }
  .person-name {
    position: absolute;
    left: 0; width: 1184px; top: 10px;
    padding-right: 16px;
    font-size: 84px; line-height: 1; font-weight: 400;
  }
  .person-role {
    position: absolute;
    left: 0; width: 1184px; top: 88px;
    padding-right: 40px;
    font-size: 34px; line-height: 1; font-weight: 400;
  }
  .contact-list {
    position: absolute;
    left: 0; width: 1184px; top: 180px;
    padding-right: 36px;
    list-style: none;
    font-size: 35px; line-height: 50px;
  }
  .service-list {
    position: absolute;
    left: 0; width: 1184px; top: 390px;
    list-style: none;
    font-size: 30px; line-height: 1;
  }
  .service-list li { position: absolute; top: 0; transform: translateX(-50%); white-space: nowrap; }
  .service-list .divider {
    width: 7px; height: 7px; top: 12px;
    background: var(--paper);
    transform: translateX(-50%) rotate(45deg);
  }
</style>
</head>
<body>
  <main class="card">
    <section class="brand-panel">
      <p class="company-name">TOLVEN Painting</p>
    </section>

    <section class="contact-panel">
      <h1 class="person-name">Marek Tolven</h1>
      <p class="person-role">Managing Director</p>
      <ul class="contact-list">
        <li>Phone: 041-527-3968</li>
        <li>Email: tolvenpainting@mail.com</li>
        <li>ABN-Number: 31 552 670 918</li>
      </ul>
      <ul class="service-list">
        <li style="left:330px">Domestic</li>
        <li class="divider" style="left:445px"></li>
        <li style="left:572px">Residential</li>
        <li class="divider" style="left:710px"></li>
        <li style="left:839px">Commercial</li>
      </ul>
    </section>
  </main>
</body>
</html>
```